Lumen Drift The Velvet Nook needs a room spray label

We are a company that is dedicated to the aromatization services for our customers, we have just created an aromatic product that is a Room Spray for the customer to spray it in their spaces and we are looking for the most sophisticated and luxurious label in the market, help us? Thanks a lot!

Target Market(s)

That the label represents an elegant and exclusive aroma

Font styles to use
Serif

Colors

Designer to choose colors to be used in the design.

Requirements
Must have
• Elegance, fine, luxury and cleanliness
Nice to have
• The fonts I like are those of the logo, they are called "Cinzel_Regular" and "MrEaveXL"
They can propose in color but I think it looks better in black and gray or white, however I would like to see something in color

```html
<!DOCTYPE html>
<html lang="en">
<head>
<meta charset="UTF-8">
<title>Lumen Drift The Velvet Nook – Room Spray Label</title>
<link rel="stylesheet" href="https://fonts.googleapis.com/css2?family=Cinzel:wght@400;500&family=Cormorant+Garamond:wght@400;500&display=swap">
<style>
  :root {
    --backdrop: #f4f3f1;
    --label-grey: #d8d5d2;
    --ink: #2b2b2b;
    --ink-soft: #4a4a4a;
    --accent-red: #b4302a;
  }
  * { margin: 0; padding: 0; box-sizing: border-box; }
  html, body {
    width: 900px;
    height: 1200px;
    overflow: hidden;
    background: var(--backdrop);
  }
  .canvas {
    width: 900px;
    height: 1200px;
    display: flex;
    align-items: center;
    justify-content: center;
  }
  .label {
    width: 640px;
    height: 1040px;
    background: var(--label-grey);
    display: flex;
    flex-direction: column;
    align-items: center;
    padding-top: 110px;
    color: var(--ink);
  }
  .brand-name {
    font-family: "Cinzel", serif;
    font-weight: 400;
    font-size: 58px;
    letter-spacing: 2px;
    line-height: 1;
    color: var(--ink);
  }
  .brand-tagline {
    font-family: "Cinzel", serif;
    font-weight: 400;
    font-size: 19px;
    letter-spacing: 5px;
    margin-top: 14px;
    color: var(--ink);
  }
  .brand-mark {
    margin-top: 60px;
  }
  .scent-name {
    margin-top: 70px;
    font-family: "Cormorant Garamond", serif;
    font-weight: 500;
    font-size: 20px;
    letter-spacing: 3px;
    color: var(--ink-soft);
  }
  .accent-rule {
    width: 46px;
    height: 3px;
    background: var(--accent-red);
    margin-top: 10px;
  }
  .product-type {
    margin-top: 16px;
    font-family: "Cinzel", serif;
    font-weight: 500;
    font-size: 50px;
    letter-spacing: 1px;
    line-height: 1;
  }
  .product-note {
    margin-top: 10px;
    font-family: "Cormorant Garamond", serif;
    font-size: 19px;
    letter-spacing: 2px;
    color: var(--ink-soft);
  }
  .volume-rule {
    width: 120px;
    height: 1px;
    background: var(--ink-soft);
    margin-top: 70px;
  }
  .volume {
    margin-top: 14px;
    font-family: "Cormorant Garamond", serif;
    font-size: 20px;
    letter-spacing: 2px;
    color: var(--ink-soft);
  }
</style>
</head>
<body>
  <main class="canvas">
    <section class="label">
      <h1 class="brand-name">LUMEN DRIFT</h1>
      <p class="brand-tagline">THE VELVET NOOK</p>
      <svg class="brand-mark" width="220" height="220" viewBox="0 0 220 220" aria-hidden="true">
        <circle cx="110" cy="110" r="100" fill="none" stroke="var(--ink)" stroke-width="6"/>
      </svg>
      <p class="scent-name">BERGAMOTTE</p>
      <div class="accent-rule"></div>
      <h2 class="product-type">ROOM SPRAY</h2>
      <p class="product-note">100% OILS BLENDS</p>
      <div class="volume-rule"></div>
      <p class="volume">100ml</p>
    </section>
  </main>
</body>
</html>
```